Counting Toward Purpose institute for nonprofits needs brochure

The Counting Toward Purpose performance management institute helps nonprofits clarify the intended impact of their programs on clients. What does a nonprofit want to accomplish - and what does it need to measure so that it can tell if they've achieved impact? The Institute is about to recruit participanting organizations. We have a lot of wording on a 2 page "flyer" that describes the institute...but it is a very ugly piece that looks unprofessional. We are looking for designs that are consistent with the KRT Advisory Group look (see our website). We are aware that we may have too much wording.

Target Market(s)

Nonprofit organization Executive Directors

Industry/Entity Type

Non-Profit

Font styles to use
Sans Serif

Requirements
Must have
• Must be able to be emailed to a client and printed on 8.5x11 paper. Doesn't matter to me if that makes it a tri-fold or two-fold.
• Need to be able to drop in later the actual dates of the program.
• Go to our website to see how we present ourselves. www.krtadvisoryhub.example
Nice to have
• See our website for KRT Advisory's "look". Our colors are green and gray (in the logo), with complementary colors of blue and orange.
• Looking for creativity in the graphics design. Our two page document has way too many words. The word impact is very important to the concept of performance management (and I'm not sure it's in the 2 page write up) - so you could do something with that word if you wanted to.
• Could use Davina's pic if it makes sense.
Should not have
• No new logo for the Counting Toward Purpose institute. It should be clear that KRT Advisory Group is the entity that offers the institute.

```html
<!DOCTYPE html>
<html lang="en">
<head>
<meta charset="utf-8">
<title>KRT Advisory – Counting Toward Purpose</title>
<link href="https://fonts.googleapis.com/css2?family=Jost:ital,wght@0,400;0,700;1,400&display=swap" rel="stylesheet">
<style>
  :root {
    --backdrop: #efefef;
    --paper: #ffffff;
    --panel: #f6f6f4;
    --ink: #1c1c1c;
    --slate: #76838a;
    --lime: #93dc12;
    --photo-a: #7a3b48;
    --photo-b: #c9a07a;
  }
  * { margin: 0; padding: 0; box-sizing: border-box; }
  html, body {
    width: 1200px; height: 1200px; overflow: hidden;
    background: var(--backdrop);
    font-family: "Jost", "Futura", sans-serif;
    color: var(--ink);
  }
  .sheet {
    position: absolute; left: 231px; top: 32px;
    width: 614px; height: 947px;
    background: var(--paper);
    transform: scale(1.2); transform-origin: top left;
  }
  .bio-panel {
    position: absolute; left: 0; top: 0; width: 614px; height: 409px;
    background: var(--panel);
  }
  .portrait {
    position: absolute; left: 28px; top: 30px; width: 142px; height: 209px;
    background: linear-gradient(160deg, var(--photo-b) 0%, #a5705a 45%, var(--photo-a) 100%);
  }
  .bio-lead {
    position: absolute; left: 188px; top: 28px; width: 400px;
    font-size: 14.6px; line-height: 19px;
  }
  .bio-lead strong, .partner strong { font-weight: 700; }
  .bio-body {
    position: absolute; left: 188px; top: 93px; width: 400px;
    font-size: 13px; line-height: 16.7px;
  }
  .bio-more {
    position: absolute; left: 28px; top: 252px; width: 562px;
    font-size: 13px; line-height: 16.9px;
  }
  .partner {
    position: absolute; left: 28px; top: 378px;
    font-size: 13px; line-height: 16.9px;
  }
  .brand {
    position: absolute; left: 30px; top: 470px;
    display: flex; align-items: center; gap: 12px;
  }
  .brand-mark {
    width: 22px; height: 22px; background: var(--slate);
  }
  .brand-name {
    font-size: 36px; font-weight: 400; color: var(--slate); line-height: 1;
  }
  .about-box {
    position: absolute; left: 360px; top: 445px; width: 254px; height: 157px;
    background: var(--panel);
    padding: 33px 28px 0 10px; text-align: right;
  }
  .about-box .founded { font-size: 14.5px; line-height: 19.4px; }
  .about-box .meaning { font-size: 13px; line-height: 17px; font-style: italic; margin-top: 7px; }
  .services {
    position: absolute; top: 617px;
    font-size: 11.4px; line-height: 14.9px;
  }
  .services p + p { margin-top: 6px; }
  .services.col-a { left: 28px; width: 272px; }
  .services.col-b { left: 316px; width: 272px; }
  .closing {
    position: absolute; left: 20px; top: 809px; width: 574px;
    text-align: center; font-size: 14.6px; line-height: 18.7px;
  }
  .closing .highlight {
    display: block; color: var(--lime); font-weight: 700; font-size: 16.4px; line-height: 20px;
  }
</style>
</head>
<body>
  <main class="sheet">
    <section class="bio-panel">
      <div class="portrait" role="img" aria-label="Portrait photo of Davina Hollis"></div>
      <p class="bio-lead"><strong>Davina Hollis</strong> joined KRT Advisory Group in 2015 as the co-designer and leader of KRT’s Counting Toward Purpose performance management institute.</p>
      <p class="bio-body">Davina is an Associate Professor of Practice at the Alder School of Social Work at Ridgeway University in Millbrook. She teaches graduate level social work practice and administration courses, including a course on program development. She is the lead teacher for Social Work Practice with Individuals, Families and Groups and serves on the Curriculum Committee as the Chair of the MSW foundations curriculum. Davina was awarded the “Excellence in Teaching” faculty award in 2011, 2010, 2008, and 2006.</p>
      <p class="bio-more">Davina co-created and co-led a highly regarded Teaching Toolbox workshop series for faculty. She currently operates an instructional coaching initiative to enhance teaching excellence at the Alder School. She conducts community trainings on Evidence Based Practice, logic models, groupwork facilitation, professional teambuilding, and adolescent development.&nbsp; Davina’s experience includes direct social work practice with adolescents in public school and health care settings, and program management experience at the Teen Pregnancy Center at Harlan Memorial Hospital.</p>
      <p class="partner">KRT Advisory Group Partner <strong>Mara Quinlan</strong> will assist on the project.</p>
    </section>

    <div class="brand">
      <span class="brand-mark" aria-hidden="true"></span>
      <span class="brand-name">KRT Advisory</span>
    </div>

    <aside class="about-box">
      <p class="founded">Founded in 2002, KRT Advisory helps nonprofits build organizational strength.</p>
      <p class="meaning">KRT stands for Knowledge, Results and Trust.</p>
    </aside>

    <div class="services col-a">
      <p>KRT Advisory provides the following types of services: planning &amp; critical decision-making (strategic planning, merger facilitation), leadership (succession, governance, coaching), fundraising (capital campaigns, development plans, operations assessment), and program development (performance management, health care/social services integration).</p>
      <p>Our partners have experience working with nonprofits from every point of view – as staff leaders, board members, and funders.&nbsp; We’ve</p>
    </div>
    <div class="services col-b">
      <p>tackled the tough issues of organizational development and change, financial and personnel management, all types of fundraising, strategic planning, marketing and communications, and board development. We’ve created nonprofits and closed them, merged them, helped them grow, helped them change, and helped them recover from a crisis.&nbsp; So, we’ve seen what works and what doesn’t, how great ideas need nurturing, and how opportunities and issues look different from different stakeholder sight lines.</p>
    </div>

    <p class="closing"><span class="highlight">We are passionate about the value of nonprofit organizations,</span>about how they touch and change lives, enliven our communities<br>and protect our environment.&nbsp; Our greatest professional satisfaction is<br>helping nonprofit organizations grow, meet challenges, overcome obstacles,<br>take calculated risks and find new opportunities to serve. Our overriding<br>professional goal is to deliver more to clients than they expect.</p>
  </main>
</body>
</html>
```